Lunar Ledger - Minimalistic Single Page Web Design

Project: We are in the process of creating a new Corp Identity. Design a website for our company incorporating the Logo recently designed and selected from a SketchHive contest. (attached)

Designers: For this project, you need to design a minimalistic single page, modern website. Beside text and image placement, you will also need to describe user interface, how content is presented and so on.
- Design Layout
- Design Image placements (if any)
- Design menu and buttons
- Design menu and buttons placements
- Design content layout
- Design overall effect and feel of website
- Design color scheme
- Design content style (tone and style of content, words type, how much)
- Design user interface (how do you scroll, what happens when you mouseover buttons, where do certain links and buttons lead you)

Coding Requirements: You need to design the website with a modern perspective on website visuals and effects. Jquery, HTML5 (no FLASH please). You do not need to code for this particular contest, but if you can also code, great, tell me and let me know how I can hire you to complete it. If you know someone that can code your vision, great, let me know. If not, you need to be clear and concise, and be willing to help me communicate with a developer to get the site executed. The web site needs to be modern and dynamic.

Company Name:
Lunar Ledger; Lunar-Ledger; LunarLedger

Domain: www.lunar-ledger.example

Company Industry:
Lunar Ledger provides consulting in areas of finance, accounting, business organization, and set up.
- Bookkeeping
- Project Management
- Budget Management
- Cash Management
- Receipt Management
- Filing and Records Management
- Training of administration and accounting staff
- Financial Reports
- Spreadsheets
- Graphs, charts and trend analysis
- Business set up
- Tax filings
- Payroll and HR

Clients:
- Small to medium size businesses
- Proprietors
- Entrepreneurs
- Mom & Pops Shops
- We cater to every industry

Corporate Identity:
- Past: I have never complete a webpage for my company. I did scratch several projects that were started and never completed. I fell in love with stick figures, whimsical designs, similar to that of "Cratebin", I believed in simplicity and minimalism. However, I was not effective in find the right people to complete my project. Bits and pieces of the website was designed, but never executed.

- Current: I need a webpage design. The web design must align with the current logo aesthetics.The current logo is new. I selected this logo for its simplicity and modern feel. It also incorporated an image of a trending graph, which fits with my company's profile. Still, I am leaning towards simple design, minimalism with boldness. I like my new webpage to be mature and professional, but I want it to portray energy and youth. So no "traditional corp" like design. I like new HTML5 elements, jquery and fun and beautiful forms and buttons. Less image is more.

Note: Please improvise according to your taste and professional perspective, you do not have to follow my suggestions word for word.

Features & Layout:
- Single page layout
- Vertical scroll
- Framed sections so that it looks good on the screen
- Well designed and strategically placed menu bar
- Fills a modern browser
- Beautiful color scheme that pops
- Incorporate Logo aesthetics

Fonts and Type:
- This is an element of the overall design
- I love clean fonts
- Fonts that adds meaning to the overall effect
- Clean

Sounds
- Please no cheesy sounds and background music

Images:
- To your liking
- But please, no lame corp people in suits
- No lame photographs
- I like stick figures
- I like whimsical illustrations

Landing Page:
- This should be the bulk of your design
- The landing page must be impressive, eye catchy
- Bold

Menu Bar:
- Header (introduction and landing page)
- Service & Products
- Company (about us)
- Affiliates and Clients (reference area)
- Contact (contact us area)
- Footer

Colors:
- Up to you, I just like things clean and easy to read
- No black background behind text
- Incorporate Logo Colors

Web Effects:
- According to your liking
- You will need to be involve to communicate the layout and design to the developer, so you need to be clear in your design.

Content:
- You personally don't have to come up with the content, but if you can great.
- I will help come up with the content throughout the contect timeframe, just let me know what you want
- I do not like too much content in my website. The most for each section is 2-3 lines if any.
- Combination could also be one liners.
- I like minimalistic approach.
- If you are not creating the final content, you need to show what type of content need to be created and in what style or tone.

Samples and Inspirations:
- http://scrollkin.example/
- http://zentrovo.example/#top
- http://brightmopservices.example/#about
- http://pixelgazette.example/inspiration/23-inspiring-single-page-designs
- http://www.tobiaskernstudio.example/
- http://www.ravelquist.example/

This I do not want:
- Too much popups (none if possible)
- Images of people
- Images of people in suits
- Stereotypical images of accountants
- Scrolling marquee
- Clip arts
Updates

Designers, I want to stress the fact that I am looking for a design, not simply a website. The website is 1 page long. Text and content should be minimal. So this means that the design has to do most of the talking. Please do not submit template like web designs, I can pull this off myself if needed. I need you to design a great header, footer and the connecting tissue from landing to end of the page. The entire design needs to flow.

Again, please do not use images of corp people or anything like that. Please think outside the box in how you want to express the company.

Some ideas:
An illustration from beginning to end of the website, have a story.
Add colors to the back ground. 
The background should not get in the way of reading the text, but it does not have to be boring.
Be bold in your design.

Also, please describe more about your design when you submit. Please don't submit a template like design and have no explanation for your actions.

Also, fee free to ask me questions. I am here to help. I check this everyday, so please contact if you need anything.

Designers, please read the details of my post before you submit the design.

If you have a great concept idea but is worry, you can go ahead and submit a pencil draft and ask my opinion before you work anymore on it.

Please see the website samples below for what I am really looking for:

Reason: Hi everyone, I am extending the deadline. It looks like some design are still pending completion, and I want you to have enough time to work on it.

Industry/Entity Type

Accounting

```html
<!DOCTYPE html>
<html lang="en">
<head>
<meta charset="utf-8">
<title>Lunar Ledger</title>
<link rel="stylesheet" href="https://fonts.googleapis.com/css2?family=Montserrat:wght@500;600&family=Lato:wght@300;400&display=swap">
<style>
  :root {
    --green: #84c31c;
    --navy: #1b1e8e;
    --ink: #111111;
    --muted: #9a9a9a;
    --body: #333333;
    --soft-bg: #f2f2f2;
    --white: #ffffff;
  }
  * { box-sizing: border-box; margin: 0; padding: 0; }
  html, body { width: 1200px; height: 2192px; overflow: hidden; background: var(--white); }
  body { font-family: "Lato", Helvetica, Arial, sans-serif; color: var(--body); position: relative; }

  .site-header {
    position: absolute; top: 0; left: 0; width: 1200px; height: 53px;
    background: var(--white); box-shadow: 0 2px 4px rgba(0,0,0,.18); z-index: 2;
  }
  .brand {
    position: absolute; left: 162px; top: 8px;
    font-family: "Montserrat", sans-serif; font-weight: 500; font-size: 25px;
    color: var(--navy); letter-spacing: .5px; text-transform: lowercase;
  }
  .main-nav { position: absolute; right: 37px; top: 20px; display: flex; gap: 33px; }
  .main-nav a {
    font-family: "Montserrat", sans-serif; font-weight: 500; font-size: 10.5px;
    color: var(--green); text-decoration: none; letter-spacing: .4px; text-transform: uppercase;
  }

  .hero { position: absolute; top: 53px; left: 0; width: 1200px; height: 466px; background: var(--soft-bg); }
  .hero-brand {
    position: absolute; top: 170px; width: 100%; text-align: center;
    font-family: "Montserrat", sans-serif; font-weight: 500; font-size: 50px;
    color: var(--navy); letter-spacing: 1px; text-transform: lowercase;
  }

  .section { position: absolute; left: 0; width: 1200px; text-align: center; }
  .section--white { background: var(--white); }
  .section--grey { background: var(--soft-bg); }
  .section-icon { position: absolute; left: 50%; transform: translateX(-50%); }
  .section-title {
    position: absolute; width: 100%;
    font-family: "Montserrat", sans-serif; font-weight: 600; font-size: 17.5px;
    color: var(--ink); letter-spacing: 1.6px; text-transform: uppercase;
  }
  .section-lead {
    position: absolute; width: 100%;
    font-weight: 300; font-size: 16.5px; line-height: 27px;
    color: var(--muted); letter-spacing: 1px;
  }

  .services { top: 519px; height: 518px; }
  .service-list { position: absolute; list-style: none; text-align: left; font-size: 13px; letter-spacing: .9px; color: var(--body); }
  .service-list li { line-height: 18px; margin-bottom: 8.6px; }
  .service-list li.tight { margin-bottom: 9px; }

  .company { top: 1037px; height: 468px; }
  .affiliates { top: 1505px; height: 334px; }
  .handshake-mark {
    width: 86px; height: 64px; border-radius: 12px;
    background: linear-gradient(135deg, #9bd23a, var(--green));
  }

  .site-footer { position: absolute; top: 1839px; left: 0; width: 1200px; height: 283px; background: var(--soft-bg); }
  .footer-col { position: absolute; top: 50px; }
  .footer-heading {
    font-family: "Montserrat", sans-serif; font-weight: 600; font-size: 13px;
    color: var(--ink); letter-spacing: 1.2px; text-transform: uppercase; margin-bottom: 15px;
  }
  .footer-col p, .footer-col a {
    display: block; font-size: 13px; line-height: 20px; color: var(--muted);
    letter-spacing: 1px; text-decoration: none; margin-bottom: 7px;
  }
  .footer-col .address { line-height: 20px; margin-bottom: 14px; }
  .social { display: flex; align-items: center; gap: 14px; margin-top: 6px; }
  .social a {
    font-family: "Lato", sans-serif; font-weight: 400; font-size: 13px;
    color: var(--green); margin: 0; letter-spacing: .4px;
  }

  .copyright {
    position: absolute; top: 2122px; left: 0; width: 1200px; height: 70px;
    padding: 24px 37px; font-size: 15px; letter-spacing: 1px; color: var(--muted);
  }
</style>
</head>
<body>

<header class="site-header">
  <div class="brand">lunarledger</div>
  <nav class="main-nav">
    <a href="#services">Service &amp; Products</a>
    <a href="#company">Company</a>
    <a href="#affiliates">Affiliates and Clients</a>
    <a href="#contact">Contact</a>
  </nav>
</header>

<section class="hero">
  <div class="hero-brand">lunarledger</div>
</section>

<section class="section section--white services" id="services">
  <svg class="section-icon" style="top:62px" width="48" height="64" viewBox="0 0 48 64" fill="none" stroke="var(--green)" stroke-width="3">
    <rect x="2" y="2" width="44" height="60"/>
    <g stroke-width="3.5">
      <line x1="17" y1="13" x2="38" y2="13"/><line x1="17" y1="20" x2="38" y2="20"/>
      <line x1="17" y1="27" x2="38" y2="27"/><line x1="17" y1="34" x2="38" y2="34"/>
      <line x1="17" y1="41" x2="38" y2="41"/><line x1="17" y1="48" x2="38" y2="48"/>
    </g>
    <circle cx="10" cy="13" r="1.2" fill="var(--green)"/>
    <circle cx="10" cy="41" r="1.2" fill="var(--green)"/>
  </svg>
  <h2 class="section-title" style="top:149px">Services &amp; Products</h2>
  <p class="section-lead" style="top:184px">Lunar Ledger provides consulting in areas of finance,<br>accounting, business organization, and set up.</p>

  <ul class="service-list" style="left:250px; top:288px">
    <li>Bookkeeping</li><li>Project Management</li><li>Budget Management</li>
    <li>Cash Management</li><li>Receipt Management</li>
  </ul>
  <ul class="service-list" style="left:540px; top:288px">
    <li style="margin-bottom:0">Filing and Records Management</li>
    <li>Training of administration</li>
    <li>and accounting staff</li><li>Financial Reports</li><li>Spreadsheets</li>
  </ul>
  <ul class="service-list" style="left:822px; top:288px">
    <li style="margin-bottom:0">Graphs, charts and</li>
    <li>trend analysis</li>
    <li>Business set up</li><li>Tax filings</li><li>Payroll and HR</li>
  </ul>
</section>

<section class="section section--grey company" id="company">
  <svg class="section-icon" style="top:68px" width="70" height="58" viewBox="0 0 70 58" fill="none" stroke="var(--green)" stroke-width="3.2" stroke-linejoin="round">
    <path d="M2 8 L2 56 L68 56 L68 8 L50 8"/>
    <path d="M2 8 Q18 2 35 12 Q52 2 68 8"/>
    <path d="M6 10 L6 52 L35 52 L35 12"/>
    <path d="M35 12 L35 52 L64 52 L64 10"/>
  </svg>
  <h2 class="section-title" style="top:155px">Company</h2>
  <p class="section-lead" style="top:187px">Lorem ipsum dolor sit amet, consectetur adipiscing elit.<br>Ut vestibulum, enim sed porttitor egestas, massa leo<br>euismod felis, eget suscipit orci lorem eget ligula.</p>
</section>

<section class="section section--white affiliates" id="affiliates">
  <div class="section-icon handshake-mark" style="top:42px" role="img" aria-label="Green line drawing of two hands shaking"></div>
  <h2 class="section-title" style="top:114px">Affiliates &amp; Clients</h2>
  <p class="section-lead" style="top:148px">Small to medium businesses, proprieters,<br>entrepeneurs, Mom &amp; Pop shops.</p>
</section>

<footer class="site-footer" id="contact">
  <div class="footer-col" style="left:245px">
    <h3 class="footer-heading">Information</h3>
    <a href="#">Choice</a><a href="#">Another Choice</a>
  </div>
  <div class="footer-col" style="left:514px">
    <h3 class="footer-heading">Company</h3>
    <a href="#">Choice</a><a href="#">Another Choice</a>
  </div>
  <div class="footer-col" style="left:802px">
    <h3 class="footer-heading">Contact</h3>
    <p class="address">Address:<br>48 Willow Bend,<br>Province, Country</p>
    <p style="margin-bottom:2px">Get in touch:</p>
    <div class="social">
      <a href="#">Chirply</a>
      <a href="#">Facenote</a>
      <svg width="24" height="18" viewBox="0 0 24 18" fill="none" stroke="var(--green)" stroke-width="2" aria-label="Email">
        <rect x="1" y="1" width="22" height="16"/>
        <path d="M1 1 L12 10 L23 1"/>
      </svg>
    </div>
  </div>
</footer>

<div class="copyright">Copyright © Lunar Ledger. 2013</div>

</body>
</html>
```